Dale Morrikan Plumbing and Heating

Need a card design for a plumbing and heating company that does service and repair, remodels, and plumbing in new construction. Please add following on back side of card; Boilers, Water heaters, Gas lines, Sump pumps, Toilet repairs, Faucet repairs, Pipe thawing, Radiant heating, New construction, Remodels.

Industry/Entity Type

Plumber

Contact Information for Business Card

Was thinking white gloss card with colored logo in middle or black glossy card with silver logo in middle. Just a thought but very open to other designs.

Requirements
Must have
• Need following on front of card;
• P(203) 321-8689
• C(203) 232-9069
• Dale Morrikan 275 Larkwell St West, Stamford, Ct 06214
• service@DrainHearth.example (plumbing in blue, heating in red)
• www.DrainHearth.example (plumbing in blue, heating in red)
• Fully Licensed and Insured
Nice to have
• Elegant design

```html
<!DOCTYPE html>
<html lang="en">
<head>
<meta charset="utf-8">
<title>Dale Morrikan Plumbing and Heating – Business Card</title>
<link rel="stylesheet" href="https://fonts.googleapis.com/css2?family=Open+Sans:wght@400;600;700&display=swap">
<style>
  :root {
    --page: #e9e6e1;
    --card: #ffffff;
    --charcoal: #38393b;
    --red: #c1222b;
    --blue: #2a54b5;
    --ink: #3b3b3b;
    --light: #f2f2f2;
    --rule: #9a9a9a;
  }
  * { box-sizing: border-box; margin: 0; padding: 0; }
  html, body { width: 1200px; height: 902px; overflow: hidden; }
  body {
    background: var(--page);
    font-family: "Open Sans", sans-serif;
    position: relative;
  }
  .card {
    position: absolute;
    left: 250px;
    width: 700px;
    height: 400px;
    background: var(--card);
    box-shadow: 0 4px 14px rgba(0,0,0,.18);
    overflow: hidden;
  }
  .card--back { top: 34px; }
  .card--front { top: 468px; }

  .brand {
    position: absolute;
    display: flex;
    align-items: center;
    gap: 14px;
    color: var(--blue);
    font-weight: 700;
    text-transform: uppercase;
    letter-spacing: 1px;
    line-height: 1.15;
  }
  .brand__dot {
    width: 18px; height: 18px; border-radius: 50%;
    background: var(--blue); flex: none;
  }
  .card--back .brand { left: 170px; top: 60px; font-size: 24px; }
  .card--front .brand { left: 60px; top: 60px; font-size: 24px; }

  .services {
    position: absolute;
    left: 120px; top: 190px;
    display: grid;
    grid-template-columns: 230px 230px;
    grid-auto-flow: column;
    grid-template-rows: repeat(5, 34px);
    list-style: none;
    font-size: 20px;
    color: var(--ink);
  }
  .services li { display: flex; align-items: center; gap: 12px; }
  .services li::before {
    content: ""; width: 9px; height: 9px; border-radius: 50%;
    border: 2px solid var(--red); flex: none;
  }

  .wave { position: absolute; inset: 0; width: 100%; height: 100%; }

  .contact { position: absolute; color: var(--light); font-size: 18px; }
  .phones { left: 60px; top: 272px; line-height: 26px; }
  .phones span { display: flex; align-items: center; gap: 10px; }
  .icon { width: 14px; height: 14px; flex: none; }
  .online { left: 380px; top: 214px; line-height: 27px; font-size: 17px; }
  .online span { display: flex; align-items: center; gap: 8px; }
  .drain { color: #5d86e6; }
  .hearth { color: #e0444c; }
  .divider {
    position: absolute; left: 360px; top: 214px;
    width: 1px; height: 110px; background: var(--light);
  }
  .address { left: 60px; top: 330px; font-size: 17px; }
  .licensed {
    position: absolute; left: 40px; right: 40px; top: 360px;
    display: flex; align-items: center; gap: 16px;
    color: var(--light); font-size: 19px; font-weight: 600;
  }
  .licensed::before, .licensed::after {
    content: ""; flex: 1; height: 1px; background: var(--rule);
  }
</style>
</head>
<body>

<section class="card card--back" aria-label="Card back">
  <div class="brand"><span class="brand__dot"></span><span>Dale Morrikan<br>Plumbing and Heating</span></div>
  <ul class="services">
    <li>Boilers</li>
    <li>Water heaters</li>
    <li>Gas lines</li>
    <li>Sump pumps</li>
    <li>Toilet repairs</li>
    <li>Faucet repairs</li>
    <li>Pipe thawing</li>
    <li>Radiant heating</li>
    <li>New construction</li>
    <li>Remodels</li>
  </ul>
</section>

<section class="card card--front" aria-label="Card front">
  <svg class="wave" viewBox="0 0 700 400" aria-hidden="true">
    <path d="M0 258 C 220 268, 420 138, 700 118 L700 400 L0 400 Z" fill="var(--red)"/>
    <path d="M0 268 C 220 278, 420 150, 700 130 L700 400 L0 400 Z" fill="var(--charcoal)"/>
  </svg>

  <div class="brand"><span class="brand__dot"></span><span>Dale Morrikan<br>Plumbing and Heating</span></div>

  <div class="contact phones">
    <span>(203) 555-0183
      <svg class="icon" viewBox="0 0 14 14"><rect x="3" y="1" width="8" height="12" rx="1.5" fill="none" stroke="currentColor" stroke-width="1.5"/></svg></span>
    <span>(203) 555-0147
      <svg class="icon" viewBox="0 0 14 14"><path d="M3 1 L5.5 4 L4 6 Q6 9 8 10 L10 8.5 L13 11 L11 13 Q5 12 1 3 Z" fill="currentColor"/></svg></span>
  </div>

  <div class="divider"></div>

  <div class="contact online">
    <span><svg class="icon" viewBox="0 0 14 14"><circle cx="7" cy="7" r="5.5" fill="none" stroke="currentColor" stroke-width="1.5"/></svg>www.<b class="drain" style="font-weight:400">Drain</b><b class="hearth" style="font-weight:400">Hearth</b>.example</span>
    <span><svg class="icon" viewBox="0 0 14 14"><rect x="1" y="3" width="12" height="8" fill="none" stroke="currentColor" stroke-width="1.5"/><path d="M1 3 L7 8 L13 3" fill="none" stroke="currentColor" stroke-width="1.5"/></svg>service@<b class="drain" style="font-weight:400">Drain</b><b class="hearth" style="font-weight:400">Hearth</b>.example</span>
  </div>

  <p class="contact address">Dale Morrikan 275 Larkwell St West, Stamford, Ct 06214</p>
  <p class="licensed">Fully Licensed and Insured</p>
</section>

</body>
</html>
```